HARBORLINE MAILWORKS - DIRECT MAIL BUSINESS CARD

Harborline Mailworks, 418 E Birch Ave, Norman OK 73512 405-287-9046 email - dalew412@mailnest.example Owner Dale Wren Serving customers since 1989, Product - Direct mail marketing

Target Market(s)

Businesses,churches and non-profits

Industry/Entity Type

Marketing

Contact Information for Business Card

Dark blue UV coated card with white letters on front. Maybe add a sketch of a mail addressing machine. On the back either Dark blue or full color with the sketch of a postman throwing a letter towards a world globe, with the phrase reach your world. Or the postman throwing a letter towards a archery target with the phrase, reach your target market.

Font styles to use
Serif

Colors
0355a3

Requirements
Must have
• INFORMATION HARBORLINE MAILWORKS
• 418 E BIRCH AVE
• NORMAN OK 73512
• 405-287-9046
• dalew412@mailnest.example
• DALE WREN, OWNER
• DIRECT MAIL MARKETING
Nice to have
• SERVING CUSTOMERS SINCE 1989 SKETCH OF MAIL ADDRESSING EQUIPMENT, IN THE BACKGROUND, ON THE FRONT
• ON THE BACK, SKETCH OF POSTMAN THROWING LETTER TO THE WORLD
• GLOBE, WITH THE PHRASE, REACH YOUR WORLD, OR THE LETTER TO A TARGET, WITH PHRASE, REACH YOUR TARGET MARKET
Should not have
• PHOTOS OR FLOWERS

```html
<!DOCTYPE html>
<html lang="en">
<head>
<meta charset="utf-8">
<title>Harborline Mailworks – Business Card</title>
<link rel="stylesheet" href="https://fonts.googleapis.com/css2?family=Noto+Serif:ital,wght@0,400;1,400&family=Cormorant+Garamond:wght@400;500&display=swap">
<style>
  :root {
    --page: #e6e7ea;
    --card-back: #0d3f7c;
    --card-back-deep: #0a3266;
    --card-front: #0355a3;
    --card-front-light: #0c66bd;
    --ink: #ffffff;
    --ink-soft: rgba(255,255,255,0.78);
    --line-soft: rgba(255,255,255,0.18);
    --art-back: rgba(140,175,220,0.35);
    --art-front: rgba(150,190,235,0.32);
  }
  * { box-sizing: border-box; margin: 0; padding: 0; }
  html, body { width: 1200px; height: 918px; overflow: hidden; background: var(--page); }
  .canvas {
    width: 1200px; height: 918px;
    display: flex; flex-direction: column; align-items: center; justify-content: center; gap: 40px;
  }
  .card {
    position: relative; width: 700px; height: 400px; overflow: hidden;
    color: var(--ink); font-family: "Noto Serif", Georgia, serif;
    box-shadow: 0 6px 18px rgba(0,0,0,0.18);
  }
  .card-back { background: radial-gradient(ellipse at 45% 45%, var(--card-back) 0%, var(--card-back-deep) 100%); }
  .card-front { background: linear-gradient(160deg, var(--card-front-light) 0%, var(--card-front) 60%); }
  .card svg.decor { position: absolute; inset: 0; width: 100%; height: 100%; }

  .art { position: absolute; border-radius: 8px; }
  .art-postman { left: 140px; top: 34px; width: 160px; height: 150px; background: radial-gradient(circle, var(--art-back), transparent 75%); }
  .art-globe { left: 480px; top: 130px; width: 130px; height: 130px; border-radius: 50%; background: radial-gradient(circle, rgba(170,200,235,0.45), rgba(120,160,215,0.2)); border: 1.5px solid var(--ink-soft); }
  .art-machine { left: 270px; top: 36px; width: 210px; height: 170px; background: radial-gradient(circle, var(--art-front), transparent 75%); }

  .tagline { position: absolute; left: 318px; top: 150px; font-style: italic; font-size: 15px; transform: rotate(24deg); transform-origin: left; }
  .owner-name { position: absolute; left: 120px; top: 252px; font-size: 38px; letter-spacing: 1px; }
  .owner-role { position: absolute; left: 124px; top: 322px; font-family: "Cormorant Garamond", Georgia, serif; font-size: 24px; letter-spacing: 3px; color: var(--ink-soft); }

  .since { position: absolute; right: 44px; top: 64px; font-size: 17px; }
  .company { position: absolute; left: 36px; top: 214px; font-size: 37px; white-space: nowrap; }
  .address { position: absolute; left: 40px; top: 300px; font-size: 19px; line-height: 1.35; }
  .contact { position: absolute; right: 40px; top: 314px; font-size: 19px; line-height: 1.5; }
  .contact-row { display: flex; align-items: center; gap: 10px; }
  .contact-row.email { font-size: 16px; }
  .contact-row svg { width: 20px; height: 20px; flex: none; }
</style>
</head>
<body>
<main class="canvas">

  <section class="card card-back" aria-label="Card back">
    <svg class="decor" viewBox="0 0 700 400" aria-hidden="true">
      <path d="M80 400 C 200 180, 420 120, 700 60" fill="none" stroke="var(--line-soft)" stroke-width="1"/>
      <path d="M60 400 C 200 200, 430 140, 700 85" fill="none" stroke="var(--line-soft)" stroke-width="1"/>
      <path d="M320 56 C 400 60, 460 100, 480 150" fill="none" stroke="var(--ink-soft)" stroke-width="1.5" stroke-dasharray="0"/>
      <path d="M472 140 L480 152 L486 138" fill="none" stroke="var(--ink-soft)" stroke-width="1.5"/>
      <line x1="110" y1="236" x2="330" y2="236" stroke="var(--ink)" stroke-width="1.2"/>
      <line x1="350" y1="306" x2="620" y2="306" stroke="var(--ink)" stroke-width="1.2"/>
      <circle cx="340" cy="306" r="3" fill="var(--ink)"/>
    </svg>
    <div class="art art-postman" role="img" aria-label="Sketch of a postman throwing a letter"></div>
    <div class="art art-globe" role="img" aria-label="Sketch of a world globe"></div>
    <p class="tagline">Reach Your World</p>
    <h2 class="owner-name">DALE WREN, OWNER</h2>
    <p class="owner-role">DIRECT MAIL MARKETING</p>
  </section>

  <section class="card card-front" aria-label="Card front">
    <svg class="decor" viewBox="0 0 700 400" aria-hidden="true">
      <path d="M0 180 C 200 120, 420 280, 700 230" fill="none" stroke="var(--line-soft)" stroke-width="1"/>
      <path d="M0 200 C 210 140, 430 300, 700 255" fill="none" stroke="var(--line-soft)" stroke-width="1"/>
      <line x1="40" y1="270" x2="330" y2="270" stroke="var(--ink)" stroke-width="1.2"/>
      <line x1="350" y1="270" x2="660" y2="270" stroke="var(--ink)" stroke-width="1.2"/>
      <circle cx="340" cy="270" r="3.5" fill="var(--ink)"/>
      <line x1="330" y1="300" x2="330" y2="380" stroke="var(--line-soft)" stroke-width="1"/>
    </svg>
    <div class="art art-machine" role="img" aria-label="Sketch of a mail addressing machine"></div>
    <p class="since">SINCE 1989</p>
    <h1 class="company">Information Harborline Mailworks</h1>
    <p class="address">418 E BIRCH AVE<br>NORMAN OK 73512</p>
    <div class="contact">
      <p class="contact-row">
        <svg viewBox="0 0 24 24" aria-hidden="true"><path d="M6.6 10.8a15 15 0 0 0 6.6 6.6l2.2-2.2a1 1 0 0 1 1-.25 11.4 11.4 0 0 0 3.6.57 1 1 0 0 1 1 1V20a1 1 0 0 1-1 1A17 17 0 0 1 3 4a1 1 0 0 1 1-1h3.5a1 1 0 0 1 1 1c0 1.25.2 2.45.57 3.57a1 1 0 0 1-.25 1z" fill="var(--ink)"/></svg>
        405-287-9046
      </p>
      <p class="contact-row email">
        <svg viewBox="0 0 24 24" aria-hidden="true"><rect x="3" y="6" width="18" height="12" fill="var(--ink)"/><path d="M3 6l9 7 9-7" fill="none" stroke="var(--card-front)" stroke-width="1.5"/></svg>
        dalew412@mailnest.example
      </p>
    </div>
  </section>

</main>
</body>
</html>
```